5x5 Pop Up Display, Company Logo With Text and Graphics for Tradeshow Display

Design for a 5ft x 5ft pop up trade show display that will sit on top of a table. I usually prefer clean, somewhat minimalist designs. We are a food service company but it's not a requirement to have photos of food. Design elements should compliment the table cloth that we have for the booth. The below may be included depending on the design aesthetic.
Service Provided: Daily Meal Service, Kitchen Management
"Nationwide Footprint"
"Grassroots Service"
"Fresh Scratch Cooking"
"Custom Menus"
"Made To Order Meals"

```html
<!DOCTYPE html>
<html lang="en">
<head>
<meta charset="utf-8">
<title>Hale Hearth — Tabletop Display</title>
<link rel="stylesheet" href="https://fonts.googleapis.com/css2?family=Exo+2:wght@500;800&display=swap">
<style>
  :root {
    --green: #3ea61c;
    --green-dark: #2f8a12;
    --ink: #141414;
    --panel-light: #f6f6f6;
    --panel-shade: #dcdcdc;
    --mark-warm: #f2b35c;
    --mark-cool: #7ccf3a;
  }
  * { margin: 0; padding: 0; box-sizing: border-box; }
  html, body {
    width: 1200px; height: 1200px; overflow: hidden;
    font-family: "Exo 2", sans-serif;
  }
  .display {
    position: relative; width: 1200px; height: 1200px;
    background: linear-gradient(90deg, var(--panel-shade) 0%, var(--panel-light) 55%, #ffffff 100%);
  }
  .header {
    position: absolute; top: 130px; left: 90px; right: 60px;
    display: flex; align-items: center;
  }
  .brand-name {
    font-weight: 800; color: var(--ink);
    font-size: 104px; line-height: 0.92; letter-spacing: 1px;
    text-transform: uppercase;
  }
  .divider {
    width: 3px; height: 230px; background: var(--green);
    margin: 0 40px 0 46px;
  }
  .tagline {
    font-weight: 800; color: var(--green);
    font-size: 74px; line-height: 0.95; text-transform: uppercase;
  }
  .mark-area {
    position: absolute; left: 470px; top: 440px;
    width: 260px; height: 480px; border-radius: 130px;
    background: radial-gradient(ellipse at 50% 65%, var(--mark-warm) 0%, #e8744a 45%, var(--mark-cool) 80%, rgba(124,207,58,0) 100%);
    opacity: 0.55;
  }
  .services {
    position: absolute; top: 990px; left: 80px; right: 60px;
    display: flex; justify-content: space-between;
  }
  .service { display: flex; align-items: center; gap: 26px; }
  .service-badge {
    width: 120px; height: 120px; border-radius: 50%;
    border: 3px solid var(--green); padding: 7px; background: #fff;
  }
  .service-badge span {
    display: block; width: 100%; height: 100%; border-radius: 50%;
    background: radial-gradient(circle at 40% 35%, var(--green) 0%, var(--green-dark) 100%);
  }
  .service-label { color: var(--green); font-size: 58px; line-height: 1; }
  .service-label .light { font-weight: 500; display: block; }
  .service-label .bold { font-weight: 800; display: block; }
</style>
</head>
<body>
  <main class="display">
    <header class="header">
      <div class="brand-name">Hale<br>Hearth</div>
      <div class="divider"></div>
      <div class="tagline">Nationwide<br>Footprint</div>
    </header>

    <div class="mark-area" role="img" aria-label="Large brand flame emblem"></div>

    <section class="services">
      <div class="service">
        <div class="service-badge" role="img" aria-label="Icon of a hand holding a serving cloche"><span></span></div>
        <p class="service-label"><span class="light">Daily Meal</span><span class="bold">Service</span></p>
      </div>
      <div class="service">
        <div class="service-badge" role="img" aria-label="Icon of a chef in a toque"><span></span></div>
        <p class="service-label"><span class="light">Kitchen</span><span class="bold">Management</span></p>
      </div>
    </section>
  </main>
</body>
</html>
```